VaultMeridan Business Card Re-Design

VaultMeridan is a specialized information security company that applies its proven methodology of security Assessment, Development, Integration and Training (A-D-I-T) to provide cyber security services in the areas of Data Protection, Network Defense and Compliance. We need the current business card re-designed to properly scale the fonts and possibly rearranging some elements (icons, lettering, etc.) to make the card more appealing to the eye. The card should have the logo that is on the web site (www.vaultmeridan-example.com). We would like ideas for both a black card (black background) and a white card (white background). We prefer rounded corners to help the card stand out but are open to all ideas. FYI: VaultMeridan's slogan is "...your security is our business".

Target Market(s)

#1 US Government Contracting Companies, #2 Commercial Companies, #3 Gen. Public.

Industry/Entity Type

Business

Contact Information for Business Card

See Description; open to the use of different fonts.

Font styles to use
Sans Serif

Colors
000000
ec1f27
ffffff

Requirements
Must have
• Company logo on web site, rounded corners, list of company offerings on the back of the card.
Nice to have
• Icons
Should not have
• none

```html
<!DOCTYPE html>
<html lang="en">
<head>
<meta charset="utf-8">
<title>VaultMeridan Business Card</title>
<link rel="stylesheet" href="https://fonts.googleapis.com/css2?family=Source+Sans+3:wght@400;600;700&display=swap">
<style>
  :root {
    --stage: #000000;
    --card: #343436;
    --card-edge: #3c3c3e;
    --ink: #ffffff;
    --ink-soft: #d9d9d9;
    --accent: #ec1f27;
    --rule: #4a4a4c;
  }
  * { box-sizing: border-box; margin: 0; padding: 0; }
  html, body {
    width: 1200px; height: 900px; overflow: hidden;
    background: var(--stage);
    font-family: "Source Sans 3", sans-serif;
    color: var(--ink);
  }
  .canvas { position: relative; width: 1200px; height: 900px; }
  .card {
    position: absolute; top: 271px;
    width: 457px; height: 281px;
    border-radius: 14px;
    background: linear-gradient(180deg, var(--card-edge), var(--card));
  }
  .card--front { left: 137px; }
  .card--back { left: 626px; }

  /* front: brand block */
  .brand {
    position: absolute; left: 30px; top: 0; width: 176px; height: 281px;
    display: flex; flex-direction: column; align-items: center; justify-content: center;
  }
  .brand__name {
    display: flex; align-items: center; gap: 8px;
    font-size: 21px; font-weight: 600; letter-spacing: 0.5px; color: var(--ink);
  }
  .brand__dot { width: 12px; height: 12px; border-radius: 50%; background: var(--accent); }
  .brand__tagline { margin-top: 10px; font-size: 11px; color: var(--ink-soft); }

  .divider {
    position: absolute; left: 221px; top: 88px; width: 1px; height: 160px;
    background: var(--rule);
  }

  /* front: details */
  .details { position: absolute; left: 239px; top: 34px; font-size: 12.5px; line-height: 19px; }
  .details__name { font-size: 16px; font-weight: 700; color: var(--accent); line-height: 20px; }
  .details__title { font-size: 12.5px; }
  .details__address { margin-top: 9px; }
  .contact-list { list-style: none; margin-top: 16px; }
  .contact-list li { display: flex; align-items: center; gap: 9px; height: 19px; }
  .contact-list svg { width: 9px; height: 9px; fill: var(--accent); flex: none; }

  /* back */
  .back-brand { position: absolute; top: 16px; left: 0; width: 100%; text-align: center; }
  .back-brand__name { font-size: 19px; font-weight: 600; letter-spacing: 0.5px; }
  .back-brand__tagline { margin-top: 6px; font-size: 10px; color: var(--ink-soft); }
  .offerings {
    position: absolute; top: 83px; left: 0; width: 100%;
    list-style: none; text-align: center;
    font-size: 13px; font-weight: 600; line-height: 19px;
    text-shadow: 0 1px 2px rgba(0,0,0,.6);
  }
  .offerings .sep {
    display: inline-block; width: 7px; height: 7px; border-radius: 50%;
    background: var(--accent); margin: 0 9px; vertical-align: 1px;
  }
</style>
</head>
<body>
<main class="canvas">
  <section class="card card--front" aria-label="Card front">
    <div class="brand">
      <div class="brand__name"><span class="brand__dot"></span>VaultMeridan</div>
      <div class="brand__tagline">Information Security Solutions</div>
    </div>
    <div class="divider"></div>
    <div class="details">
      <div class="details__name">Marcus Hale</div>
      <div class="details__title">President-CEO CISSP, C|EH</div>
      <div class="details__address">
        VaultMeridan, Inc,<br>
        4120 Harlow Rd.Suite 210<br>
        Brenton,Maryland 21099
      </div>
      <ul class="contact-list">
        <li><svg viewBox="0 0 10 10"><path d="M2 0l2 2.5-1.2 1.2c.6 1.3 1.5 2.2 2.5 2.8L6.5 5.3 10 7.5 8.5 10C4 9.5.5 6 0 1.5z"/></svg>240.555.0143</li>
        <li><svg viewBox="0 0 10 10"><path d="M2.5 0h5v10h-5zM3.5 1v7h3V1z"/></svg>301.555.0178</li>
        <li><svg viewBox="0 0 10 10"><path d="M0 2h10v6H0zM.8 2.6L5 5.6l4.2-3z" fill-rule="evenodd"/></svg>info@vaultmeridan-example.com</li>
        <li><svg viewBox="0 0 10 10"><path d="M0 2h10v6H0zM.8 2.6L5 5.6l4.2-3z" fill-rule="evenodd"/></svg>mhale@vaultmeridan-example.com</li>
        <li><svg viewBox="0 0 10 10"><circle cx="5" cy="5" r="5"/></svg>www.vaultmeridan-example.com</li>
      </ul>
    </div>
  </section>

  <section class="card card--back" aria-label="Card back">
    <div class="back-brand">
      <div class="back-brand__name">VaultMeridan</div>
      <div class="back-brand__tagline">Information Security Solutions</div>
    </div>
    <ul class="offerings">
      <li>Secure Cloud &amp; Open Stack Solution</li>
      <li>Network Attack Penetration &amp; Defense<span class="sep"></span>Red/Blue Team</li>
      <li>Data Centre Consolidation<span class="sep"></span>Secure Virtual Computing</li>
      <li>Clssified Cross Domain Solution</li>
      <li>Foreign/Counter Intelligence Data Security</li>
      <li>Certifiction &amp; Accreditation<span class="sep"></span>Secure Wireless Solution</li>
      <li>Security Training, Assessment &amp; Integration</li>
      <li>Security Subject Matter Experts</li>
      <li>Executive Security Strategy Coaching<span class="sep"></span>Date Encryption/Privacy</li>
    </ul>
  </section>
</main>
</body>
</html>
```